Business start up

I need a logo within the business cards that has the name brontz with two racing stripes like the vexor racing stripes next to the name .... one of the stripes I would want to have the shades of window tint and the other stripe the colors of vinyl wrap or even the name having dripping paint of the different colors in it ... it will be a business of window tint and vinyl wrap .... service that I will be providing would be window tint Vinyl wrap Paint protection (ppfTaillights/headlights tintsBlackouts/Chrome delete Decals

Target Market(s)

Automotive

Industry/Entity Type

Automotive

Contact Information for Business Card

Have the name brontz drip like paint and have different colors dripping

Font styles to use
Serif
Sans Serif
Decorative
Script

Colors

Designer to choose colors to be used in the design.

Requirements
Nice to have
• I need a logo within the business cards that has the name brontz with two racing stripes like the vexor racing stripes next to the name .... one of the stripes I would want to have the shades of window tint and the other stripe the colors of vinyl wrap or even the name having dripping paint of the different colors in it ... it will be a business of window tint and vinyl wrap .... service that I will be providing would be
• window tint
• Vinyl wrap
• Paint protection (ppf
• Taillights/headlights tints
• Blackouts/Chrome delete
• Decals

```html
<!DOCTYPE html>
<html lang="en">
<head>
<meta charset="utf-8">
<title>Brontz Business Card</title>
<link href="https://fonts.googleapis.com/css2?family=Saira:ital,wght@0,700;1,600&display=swap" rel="stylesheet">
<style>
  :root {
    --bg: #2a2a2c;
    --card: #121216;
    --gold: #e8d35a;
    --orange: #ef4b24;
    --white: #ffffff;
  }
  * { margin: 0; padding: 0; box-sizing: border-box; }
  html, body { width: 1200px; height: 900px; overflow: hidden; }
  body {
    background: var(--bg);
    font-family: "Saira", sans-serif;
    position: relative;
  }
  .card {
    position: absolute;
    left: 250px;
    width: 700px;
    height: 400px;
    background: var(--card);
    overflow: hidden;
    box-shadow: 0 10px 30px rgba(0,0,0,0.5);
  }
  .card-front { top: 40px; }
  .card-back { top: 460px; }
  .band { position: absolute; right: 0; }
  .brand {
    position: absolute;
    display: flex;
    align-items: center;
    gap: 14px;
    color: var(--gold);
    font-weight: 700;
    font-size: 52px;
    letter-spacing: 2px;
    line-height: 1;
  }
  .brand-mark {
    width: 16px; height: 16px;
    background: var(--gold);
  }
  .card-front .brand { left: 60px; top: 110px; }
  .card-back .brand { left: 60px; top: 60px; }
  .services {
    position: absolute;
    left: 50px; right: 30px; top: 262px;
    color: var(--gold);
    font-style: italic;
    font-weight: 600;
    font-size: 17px;
    letter-spacing: 1.5px;
    line-height: 1.6;
    text-transform: uppercase;
  }
  .services span::before {
    content: "";
    display: inline-block;
    width: 5px; height: 5px;
    background: var(--orange);
    margin: 0 7px 3px 4px;
  }
  .person {
    position: absolute;
    right: 40px; top: 130px;
    text-align: right;
    color: var(--white);
    font-style: italic;
    font-weight: 600;
    text-transform: uppercase;
    letter-spacing: 1.5px;
  }
  .person-name { font-size: 24px; line-height: 1.1; }
  .person-role { font-size: 16px; letter-spacing: 3px; }
  .contacts {
    position: absolute;
    left: 60px; top: 270px;
    list-style: none;
    color: var(--gold);
    font-style: italic;
    font-weight: 600;
    font-size: 20px;
    letter-spacing: 2px;
    line-height: 1.55;
    text-transform: uppercase;
  }
  .contacts li { display: flex; align-items: center; gap: 12px; }
  .contacts svg { width: 16px; height: 16px; flex: none; }
</style>
</head>
<body>
  <section class="card card-front">
    <svg class="band" width="330" height="110" viewBox="0 0 330 110" style="top:150px" aria-hidden="true">
      <path d="M0 60 L70 8 Q80 0 95 0 L330 0 L330 110 Z" fill="var(--orange)"/>
    </svg>
    <div class="brand"><span class="brand-mark"></span>BRONTZ</div>
    <p class="services">
      <span>Window tint</span> <span>Vinyl wrap</span> <span>Paint protection (PPF</span><br>
      <span>Taillights/headlights tints</span> <span>Blackouts/chrome delete</span> <span>Decals</span>
    </p>
  </section>

  <section class="card card-back">
    <svg class="band" width="440" height="110" viewBox="0 0 440 110" style="top:110px" aria-hidden="true">
      <path d="M0 110 L78 10 Q86 0 100 0 L440 0 L440 110 Z" fill="var(--orange)"/>
    </svg>
    <div class="brand"><span class="brand-mark"></span>BRONTZ</div>
    <div class="person">
      <p class="person-name">Marek Volansky</p>
      <p class="person-role">Manager</p>
    </div>
    <ul class="contacts">
      <li>
        <svg viewBox="0 0 16 16" aria-hidden="true"><path d="M4 1 L6.5 4.5 L5 6.5 Q6.5 9.5 9.5 11 L11.5 9.5 L15 12 L13 15 Q6 14 1 3 Z" fill="var(--orange)"/></svg>
        (555) 210/4478
      </li>
      <li>
        <svg viewBox="0 0 16 16" aria-hidden="true"><rect x="1" y="3" width="14" height="10" fill="none" stroke="var(--orange)" stroke-width="1.5"/><path d="M1 3 L8 9 L15 3" fill="none" stroke="var(--orange)" stroke-width="1.5"/></svg>
        info@brontz.com
      </li>
      <li>
        <svg viewBox="0 0 16 16" aria-hidden="true"><circle cx="8" cy="8" r="6.5" fill="none" stroke="var(--orange)" stroke-width="1.3"/><ellipse cx="8" cy="8" rx="3" ry="6.5" fill="none" stroke="var(--orange)" stroke-width="1.1"/><path d="M1.5 8 H14.5 M3 4.5 H13 M3 11.5 H13" stroke="var(--orange)" stroke-width="1.1"/></svg>
        www.brontz.com
      </li>
    </ul>
  </section>
</body>
</html>
```